Business Cards for Life Coaching Practice
RVT Harbor Ltd
Business Cards for Life Coaching Practice - Consulting
Creative Brief
Professional
Dovinder Plume
admin@rvtharbor.co.uk
brightpathmentoring.co.uk
Please show me both 1 side and 2 sided options. I have uploaded logo files and would like to see design options using the colour schemes.
"Be True To Yourself" ------Your Journey-------
RVTHARBOR RVTHARBOR
please only send me designs on plastic cards.
sevensky sevensky
Its Done! check your private messages on top right side messages (1) thanks!
#33 please can you provide different colour backgrounds for this design?
Its Done! thanks
#32 Please apply this back to designs #23 - #25 and #27 - #29
#22 the blue stone is too big for the card and needs to be smaller to fit on the card
#14 I like the plastic shine type card. As stated i would like the statement on back and stones need to be on card
#7 I like the wave concept. The back is however too dark and I want "be true to yourself" on the back.

```html
<!DOCTYPE html>
<html lang="en">
<head>
<meta charset="utf-8">
<title>RVT Harbor Ltd – Business Cards</title>
<link rel="stylesheet" href="https://fonts.googleapis.com/css2?family=Cinzel:wght@400;600&display=swap">
<style>
  :root {
    --backdrop: #e6e9ec;
    --card: #ffffff;
    --card-edge: #d4d8dc;
    --ink: #2f6f93;
    --ink-soft: #5d7f94;
    --wave-blue: #1e6fb3;
    --wave-light: #5fa3d6;
    --wave-grey: #9aa3a9;
    --dot: #6fb0c9;
    --name-light: #ffffff;
  }
  * { box-sizing: border-box; margin: 0; padding: 0; }
  html, body {
    width: 1200px;
    height: 980px;
    overflow: hidden;
    background: var(--backdrop);
    font-family: "Cinzel", serif;
  }
  .sheet {
    width: 1200px;
    height: 980px;
    display: flex;
    flex-direction: column;
    align-items: center;
    justify-content: center;
    gap: 40px;
  }
  .card {
    position: relative;
    width: 740px;
    height: 430px;
    background: var(--card);
    border: 1px solid var(--card-edge);
    border-radius: 26px;
    overflow: hidden;
  }
  .brand {
    position: absolute;
    display: flex;
    align-items: center;
    gap: 16px;
  }
  .brand-dot {
    width: 38px;
    height: 38px;
    border-radius: 50%;
    background: var(--dot);
  }
  .brand-name {
    font-family: "Cinzel", serif;
    font-weight: 600;
    font-size: 44px;
    letter-spacing: 1px;
    color: var(--ink);
  }
  .brand-rule {
    position: absolute;
    border-top: 2px dotted var(--wave-grey);
  }

  /* Back side */
  .card-back .brand { left: 200px; top: 160px; }
  .card-back .brand-rule.top { left: 190px; top: 140px; width: 380px; }
  .card-back .brand-rule.bottom { left: 190px; top: 240px; width: 380px; }

  /* Front side */
  .card-front .brand { left: 320px; top: 56px; }
  .card-front .brand-rule.bottom { left: 310px; top: 126px; width: 380px; }
  .wave { position: absolute; inset: 0; width: 100%; height: 100%; }
  .contact-list {
    position: absolute;
    left: 42px;
    top: 122px;
    list-style: none;
    display: flex;
    flex-direction: column;
    gap: 6px;
    font-size: 14px;
    line-height: 20px;
    color: var(--ink-soft);
  }
  .contact-list li { display: flex; align-items: center; gap: 10px; }
  .contact-icon { width: 16px; height: 16px; flex: none; }
  .holder-name {
    position: absolute;
    right: 44px;
    bottom: 12px;
    font-size: 22px;
    letter-spacing: 2px;
    color: var(--name-light);
  }
</style>
</head>
<body>
<main class="sheet">

  <section class="card card-back" aria-label="Card back">
    <div class="brand-rule top"></div>
    <div class="brand">
      <span class="brand-dot"></span>
      <span class="brand-name">RVTHARBOR</span>
    </div>
    <div class="brand-rule bottom"></div>
  </section>

  <section class="card card-front" aria-label="Card front">
    <svg class="wave" viewBox="0 0 740 430" preserveAspectRatio="none" aria-hidden="true">
      <path d="M0,282 C180,340 430,375 740,352" fill="none" stroke="var(--wave-grey)" stroke-width="5"/>
      <path d="M0,306 C190,358 440,390 740,372 L740,430 L0,430 Z" fill="var(--wave-light)"/>
      <path d="M0,320 C190,370 440,400 740,384 L740,430 L0,430 Z" fill="var(--wave-blue)"/>
    </svg>

    <div class="brand">
      <span class="brand-dot"></span>
      <span class="brand-name">RVTHARBOR</span>
    </div>
    <div class="brand-rule bottom"></div>

    <ul class="contact-list">
      <li>
        <svg class="contact-icon" viewBox="0 0 16 16" aria-hidden="true"><circle cx="8" cy="8" r="8" fill="var(--wave-light)"/><path d="M5 4.5l1.6-.5 1 2.2-1 .8a5 5 0 0 0 2.4 2.4l.8-1 2.2 1-.5 1.6c-3.3.3-6.8-3.2-6.5-6.5z" fill="#fff"/></svg>
        <span>020 7946 0321</span>
      </li>
      <li>
        <svg class="contact-icon" viewBox="0 0 16 16" aria-hidden="true"><circle cx="8" cy="8" r="8" fill="var(--wave-light)"/><rect x="5.5" y="3.5" width="5" height="9" rx="1" fill="#fff"/></svg>
        <span>07700 900 482</span>
      </li>
      <li>
        <svg class="contact-icon" viewBox="0 0 16 16" aria-hidden="true"><circle cx="8" cy="8" r="8" fill="var(--wave-light)"/><rect x="4" y="5" width="8" height="6" fill="#fff"/><path d="M4 5l4 3 4-3" fill="none" stroke="var(--wave-light)"/></svg>
        <span>admin@rvtharbor.co.uk</span>
      </li>
      <li>
        <svg class="contact-icon" viewBox="0 0 16 16" aria-hidden="true"><circle cx="8" cy="8" r="8" fill="var(--wave-light)"/><circle cx="8" cy="8" r="4" fill="none" stroke="#fff"/><path d="M4 8h8M8 4v8" stroke="#fff"/></svg>
        <span>www.rvtharbor.co.uk</span>
      </li>
      <li>
        <svg class="contact-icon" viewBox="0 0 16 16" aria-hidden="true"><circle cx="8" cy="8" r="8" fill="var(--wave-light)"/><circle cx="8" cy="8" r="4" fill="none" stroke="#fff"/><path d="M4 8h8M8 4v8" stroke="#fff"/></svg>
        <span>www.brightpathmentoring.co.uk</span>
      </li>
    </ul>

    <p class="holder-name">DOVINDER PLUME</p>
  </section>

</main>
</body>
</html>
```